Vindhalur - Start-up company selling electricity

Hello let me tell you about Vindhalur.

Vindhalur is start-up company selling electricity in Iceland. The operations of the company consist of making power usage forecasts for our customers, purchasing the electricity wholesale from the energy producers, and selling the electricity to the consumer. We are focused on tech by using optimization and machine learning to minimize electricity prices to our customers. Our marketing strategy is to portray a tech company mindset and to show dedication to driving down the electricity price on the market.

We need your help to make our website pop. Possible concepts to work with are as follows:

- Iceland the land of ice and fire
- Green energy
- Innovation
- Tech and data science

Link to our website: https://demo.vindhalur-example.is/
We are open to ideas.
Thank you!

Target Market(s)

Electricity consumers both homes and companies.

Number of Pages Required

1 page

Font styles to use
Serif
Sans Serif

```html
<!DOCTYPE html>
<html lang="is">
<head>
<meta charset="utf-8">
<title>Vindhalur</title>
<link href="https://fonts.googleapis.com/css2?family=Poppins:wght@400;500;600&family=Libre+Baskerville:wght@700&display=swap" rel="stylesheet">
<style>
:root{
  --navy:#06336b;
  --navy-deep:#0b2a57;
  --red:#9a3034;
  --red-bright:#a52a2f;
  --grey:#8a8a8a;
  --text:#6f6f6f;
  --dark:#3a3a3a;
  --white:#ffffff;
}
*{margin:0;padding:0;box-sizing:border-box}
html,body{width:773px;height:1200px;overflow:hidden;background:var(--white)}
body{position:relative;font-family:'Poppins',sans-serif;color:var(--text)}
.abs{position:absolute}
.topbar{left:0;top:0;width:773px;height:24px;background:var(--navy);color:var(--white);font-size:7.5px}
.topbar span{position:absolute;top:7px}
.topbar .sep{left:613px;top:6px;width:1px;height:12px;background:#2f6bb0}
.navbar{left:0;top:24px;width:773px;height:32px;background:var(--white);border-bottom:1px solid #9bb7d6}
.brand{display:flex;align-items:center;gap:6px;font-family:'Libre Baskerville',serif;font-weight:700;font-size:17px;color:var(--red-bright);letter-spacing:.3px;white-space:nowrap}
.brand .dot{width:20px;height:20px;border-radius:50%;background:var(--navy)}
.navbar .brand{position:absolute;left:38px;top:5px}
.nav{position:absolute;top:12px;font-size:8px;color:#555;white-space:nowrap}
.nav.active{color:var(--red-bright)}
.hero{left:0;top:56px;width:773px;height:372px;background:linear-gradient(180deg,#083569 0%,#1c5aa0 35%,#6f9cd0 58%,#d4c9b2 70%,#5f8fc7 82%,#2e67ad 100%)}
.hero-title{left:0;top:140px;width:773px;text-align:center;font-family:'Libre Baskerville',serif;font-weight:700;font-size:33px;color:var(--white);letter-spacing:1px}
.hero-sub{left:186px;top:190px;width:400px;text-align:center;font-size:10.5px;line-height:15.5px;color:var(--white);letter-spacing:.2px;white-space:nowrap}
.cta{left:335px;top:236px;width:104px;height:27px;border-radius:14px;background:var(--red-bright);color:var(--white);font-size:9px;display:flex;align-items:center;padding-left:10px;box-shadow:2px 2px 4px rgba(0,0,0,.25);white-space:nowrap}
.cta .knob{position:absolute;right:3px;top:3px;width:21px;height:21px;border-radius:50%;background:var(--white)}
.ring{width:64px;height:64px;border-radius:50%;border:1.3px solid;display:flex;align-items:center;justify-content:center}
.ring.navy{border-color:var(--navy-deep)}
.ring.red{border-color:var(--red)}
.ring.grey{border-color:var(--grey)}
.feature h2{position:absolute;font-size:11px;font-weight:600;white-space:nowrap}
.feature p{position:absolute;font-size:7.8px;line-height:12.5px;color:var(--text)}
.btn{position:absolute;height:27px;display:flex;align-items:center;justify-content:center;font-size:8px;font-weight:600;border-radius:2px;white-space:nowrap}
.btn.navy{background:var(--navy);color:var(--white)}
.btn.outline{border:1px solid var(--navy);color:var(--navy);background:var(--white)}
.btn.red{background:var(--red);color:var(--white)}
.btn.grey{background:var(--grey);color:var(--white)}
.price{position:absolute;font-size:17px;color:var(--dark)}
.unit{position:absolute;font-size:8px;color:var(--text);white-space:nowrap}
.art{left:478px;top:480px;width:256px;height:388px;border-radius:128px;background:linear-gradient(180deg,#c06b63 0%,#a14b43 42%,#21407a 58%,#122d5e 100%)}
.footer{left:0;top:966px;width:773px;height:210px;background:var(--red);color:var(--white)}
.footer .brand{position:absolute;left:39px;top:42px;color:var(--white);font-size:15px}
.footer .brand .dot{background:var(--white);width:16px;height:16px}
.footer .about{position:absolute;left:39px;top:72px;width:154px;font-size:7.8px;line-height:12.5px}
.footer h3{position:absolute;top:40px;font-size:11.5px;font-weight:400;white-space:nowrap}
.footer ul{position:absolute;list-style:none;font-size:7.8px;white-space:nowrap}
.footer li::before{content:"- "}
.contact-icon{position:absolute;left:393px;width:22px;height:22px;background:var(--white);display:flex;align-items:center;justify-content:center}
.contact-text{position:absolute;left:423px;font-size:7.5px;white-space:nowrap}
.bottombar{left:0;top:1176px;width:773px;height:24px;background:var(--navy);color:var(--white);font-size:7.5px;text-align:center;line-height:24px}
</style>
</head>
<body>

<div class="abs topbar">
  <span style="left:509px">VAT number: 100248</span>
  <span class="sep"></span>
  <span style="left:637px">ID Number: 010101-0990</span>
</div>

<header class="abs navbar">
  <div class="brand"><span class="dot"></span>VINDHALUR</div>
  <span class="nav active" style="left:429px">Home</span>
  <span class="nav" style="left:474px">Terms of Business</span>
  <span class="nav" style="left:568px">Question &amp; Answer</span>
  <span class="nav" style="left:666px">About Vindhalur</span>
</header>

<section class="abs hero" role="img" aria-label="Photograph of a lakeside Icelandic town with a church and colourful houses reflected in calm water under a deep blue sky"></section>
<div class="abs hero-title">VINDHALUR</div>
<div class="abs hero-sub">Vindhalur reserves the right to change these<br>terms of business.</div>
<div class="abs cta">CONTACT US<span class="knob"></span></div>

<div class="feature">
  <div class="abs ring navy" style="left:38px;top:531px">
    <svg width="40" height="28" viewBox="0 0 40 28" fill="none" stroke="#0b2a57" stroke-width="1.6" stroke-linecap="round" stroke-linejoin="round">
      <path d="M2 6h6v14H2M38 6h-6v14h6"/><path d="M8 8l8-3 6 3 5-2 5 2M8 18l5 5 3-1 3 2 3-1 4 1 6-6"/><path d="M22 8l-5 5 3 1 5-3 7 7"/>
    </svg>
  </div>
  <h2 style="left:122px;top:542px;color:var(--navy-deep)">Velkomin í viðskipti</h2>
  <p style="left:122px;top:562px;width:220px">Lorem Ipsum is simply dummy text of the printing and typesetting industry.</p>
  <div class="btn navy" style="left:121px;top:594px;width:77px">Fyrirtæki</div>
  <div class="btn outline" style="left:208px;top:594px;width:68px">Heimili</div>
</div>

<div class="feature">
  <div class="abs ring red" style="left:38px;top:652px">
    <svg width="34" height="30" viewBox="0 0 34 30" fill="none" stroke="#9a3034" stroke-width="1.6" stroke-linecap="round">
      <rect x="2" y="3" width="18" height="24" rx="2"/><path d="M6 10h8M6 15h6M6 20h8"/><circle cx="24" cy="14" r="7"/><path d="M24 9v10M26.5 11.5c-1-1-5-1-5 1s5 1 5 3-4 2-5 1"/>
    </svg>
  </div>
  <h2 style="left:122px;top:663px;color:var(--red)">Verðskrá</h2>
  <span class="price" style="left:129px;top:680px">6.98</span>
  <span class="unit" style="left:122px;top:703px">krónur / kWst</span>
  <span class="abs" style="left:193px;top:682px;width:1px;height:31px;background:#ddd"></span>
  <span class="price" style="left:222px;top:680px">6.25</span>
  <span class="unit" style="left:214px;top:703px">krónur / kWst</span>
  <p style="left:122px;top:726px;width:100px">rafmagnskynding<br>Gerðu verðsamanburð</p>
  <div class="btn red" style="left:227px;top:726px;width:78px">Verðvaki</div>
</div>

<div class="feature">
  <div class="abs ring grey" style="left:38px;top:787px">
    <svg width="38" height="30" viewBox="0 0 38 30" fill="none" stroke="#7d7d7d" stroke-width="1.5" stroke-linecap="round" stroke-linejoin="round">
      <path d="M7 16a12 12 0 0 1 21-9M31 14a12 12 0 0 1-21 9"/><path d="M3 12l4 4 4-4M35 18l-4-4-4 4"/><path d="M21 5l-6 11h6l-4 9 8-12h-6l3-8z"/>
    </svg>
  </div>
  <h2 style="left:122px;top:797px;color:var(--dark)">Framtíðin er spennandi</h2>
  <p style="left:122px;top:817px;width:225px">Gerum raforkukerfið snallara saman. Vindhalur notar gervigreind, gagnavísindi og sjálfvirkni til að lágmarka kostnað og stuðla að okrujöfnuði</p>
  <div class="btn grey" style="left:121px;top:866px;width:77px">Vita Meira</div>
</div>

<div class="abs art" role="img" aria-label="Illustration combining a red mountain sunrise above and a blue night view of Earth with glowing network lines below"></div>

<footer class="abs footer">
  <div class="brand"><span class="dot"></span>VINDHALUR</div>
  <p class="about">Our marketing strategy is to portray a tech company mindset and to show dedication to driving down the electricity price on the market.</p>

  <h3 style="left:217px">Site Map</h3>
  <ul style="left:217px;top:60px;line-height:19.5px">
    <li>Home</li><li>Terms of Business</li><li>Question &amp; Answer</li><li>About Vindhalur</li>
  </ul>

  <h3 style="left:394px">Contact Us</h3>
  <div class="contact-icon" style="top:60px">
    <svg width="12" height="14" viewBox="0 0 12 14" fill="none" stroke="#9a3034" stroke-width="1.3"><path d="M6 13s4.5-4.5 4.5-7.5a4.5 4.5 0 0 0-9 0C1.5 8.5 6 13 6 13z"/><circle cx="6" cy="5.5" r="1.6"/></svg>
  </div>
  <span class="contact-text" style="top:67px">Hafnargata 7, 200 Vesturbær</span>
  <div class="contact-icon" style="top:94px">
    <svg width="13" height="10" viewBox="0 0 13 10"><rect width="13" height="10" rx="1" fill="#9a3034"/><path d="M1 1.5l5.5 4 5.5-4" fill="none" stroke="#fff" stroke-width="1.2"/></svg>
  </div>
  <span class="contact-text" style="top:101px">info@vindhalur-example.is</span>
  <div class="contact-icon" style="top:128px">
    <svg width="12" height="12" viewBox="0 0 12 12"><path d="M2.5 1l2 2.5-1.2 1.5a7 7 0 0 0 3.7 3.7L8.5 7.5 11 9.5 9.5 11.5C4.5 11 1 7.5.5 2.5z" fill="#9a3034"/></svg>
  </div>
  <span class="contact-text" style="top:137px">555-0199</span>

  <h3 style="left:572px">Terms of Business</h3>
  <ul style="left:572px;top:63px;line-height:14.6px">
    <li>Scope</li><li>Gathering information and plan</li><li>Dealer change</li><li>User exchange</li><li>Prices and payment terms</li><li>End of contractual relationship</li><li>Privacy</li><li>Uncontrollable events</li>
  </ul>
</footer>

<div class="abs bottombar">©2021 VINDHALUR - All Right Reserved.</div>

</body>
</html>
```